Bright Oak Fitness Facility Business Cards

Business Card Design that incorporates the logo and tagline

Target Market(s)

Fitness, People Who Exercise

Contact Information for Business Card

2817 Mossgrove Bend Road
Lakemont, Oregon 97190
Phone: 541-555-Jump (5867)
www.brightoakfitness.example
info@brightoakfitness.example

Requirements
Must have
• Logo, Address, Website, email and tagline "Stronger Every Day". Colors should be red/black/grey/white

```html
<!DOCTYPE html>
<html lang="en">
<head>
<meta charset="utf-8">
<title>Bright Oak Fitness Facility – Business Cards</title>
<link href="https://fonts.googleapis.com/css2?family=Carlito:wght@400;700&display=swap" rel="stylesheet">
<style>
  :root {
    --board-red: #e3120f;
    --brand-red: #d9343f;
    --deep-red: #96222c;
    --card-black: #000000;
    --frame-black: #1c1c1c;
    --sheen: #1f1f1f;
    --slate: #5a5c5c;
    --stone: #5b5b5b;
    --ink-white: #ffffff;
  }
  html, body {
    margin: 0;
    width: 1200px;
    height: 1200px;
    overflow: hidden;
    background: var(--board-red);
  }
  .presentation-board {
    display: block;
    width: 1200px;
    height: 1200px;
  }
  .option-number {
    font-family: "Carlito", sans-serif;
    font-size: 90px;
    fill: #111;
  }
  .contact-text {
    font-family: "Carlito", sans-serif;
    font-size: 35px;
    fill: var(--ink-white);
  }
  .tagline {
    font-family: "Carlito", sans-serif;
    fill: var(--ink-white);
  }
  .brand-name {
    font-family: "Carlito", sans-serif;
    font-weight: 700;
    fill: var(--brand-red);
  }
  .icon-ring { fill: none; stroke: var(--brand-red); stroke-width: 3; }
  .icon-glyph { fill: var(--brand-red); }
  .icon-line { fill: none; stroke: var(--brand-red); stroke-width: 2.5; }
</style>
</head>
<body>
<svg class="presentation-board" viewBox="0 0 1500 1500" xmlns="http://www.w3.org/2000/svg" aria-label="Two business card options for Bright Oak Fitness Facility">
  <defs>
    <filter id="red-glow" x="-10%" y="-15%" width="120%" height="130%">
      <feDropShadow dx="0" dy="0" stdDeviation="14" flood-color="#ff6a6a" flood-opacity="0.9"/>
    </filter>
    <filter id="card-shadow" x="-10%" y="-15%" width="120%" height="130%">
      <feDropShadow dx="0" dy="4" stdDeviation="12" flood-color="#300000" flood-opacity="0.75"/>
    </filter>
  </defs>

  <!-- Option 3 -->
  <text class="option-number" x="181" y="202">3</text>
  <g class="card card-option-3">
    <rect x="285" y="113" width="1062" height="595" fill="var(--card-black)" filter="url(#red-glow)"/>
    <rect x="298" y="136" width="1030" height="547" fill="var(--frame-black)"/>
    <rect x="630" y="136" width="683" height="531" fill="var(--card-black)"/>
    <polygon points="640,136 1313,136 1313,158 715,345" fill="var(--sheen)"/>
    <path d="M300,138 L632,138 Q718,280 718,410 Q718,560 632,682 L300,682 Z" fill="var(--card-black)"/>
    <path class="front-panel" d="M300,138 L615,138 Q703,280 703,410 Q703,560 615,682 L300,682 Z" fill="var(--stone)" stroke="var(--brand-red)" stroke-width="4"/>
    <text class="brand-name" x="500" y="362" font-size="44" text-anchor="middle">Bright Oak Fitness</text>
    <text class="tagline" x="315" y="586" font-size="38">"Stronger Every Day"</text>

    <g class="contact-icon icon-pin">
      <circle class="icon-ring" cx="788" cy="255" r="22"/>
      <path class="icon-line" d="M788,266 C780,256 780,250 780,247 A8,8 0 0 1 796,247 C796,250 796,256 788,266 Z"/>
      <path class="icon-line" d="M776,264 Q788,272 800,264"/>
    </g>
    <text class="contact-text" x="825" y="250">2817 Mossgrove Bend Road</text>
    <text class="contact-text" x="827" y="282">Lakemont, Oregon 97190</text>

    <g class="contact-icon icon-phone">
      <circle class="icon-ring" cx="797" cy="362" r="22"/>
      <path class="icon-glyph" d="M786,351 l6,-2 4,8 -4,3 q3,7 10,10 l3,-4 8,4 -2,6 q-18,2 -25,-25 z"/>
    </g>
    <text class="contact-text" x="832" y="374">541-555-Jump (5867)</text>

    <g class="contact-icon icon-mail">
      <circle class="icon-ring" cx="796" cy="469" r="22"/>
      <rect class="icon-glyph" x="783" y="460" width="24" height="17" rx="2"/>
      <path d="M783,461 L795,470 L807,461" stroke="var(--card-black)" stroke-width="2" fill="none"/>
    </g>
    <text class="contact-text" x="832" y="481">info@brightoakfitness.example</text>

    <g class="contact-icon icon-globe">
      <circle class="icon-ring" cx="784" cy="572" r="22"/>
      <circle class="icon-line" cx="784" cy="572" r="15"/>
      <ellipse class="icon-line" cx="784" cy="572" rx="6" ry="15"/>
      <path class="icon-line" d="M769,572 H799 M772,564 H796 M772,580 H796"/>
    </g>
    <text class="contact-text" x="820" y="584">www.brightoakfitness.example</text>
  </g>

  <!-- Option 4 -->
  <text class="option-number" x="1278" y="928">4</text>
  <g class="card card-option-4">
    <rect x="165" y="815" width="1063" height="590" fill="var(--slate)" filter="url(#card-shadow)"/>
    <polygon points="755,835 1210,835 1210,1387 385,1387" fill="var(--card-black)"/>
    <polygon points="708,916 757,840 1205,843" fill="var(--brand-red)"/>
    <polygon points="712,922 1205,848 1205,922" fill="var(--deep-red)"/>
    <polygon points="392,1383 442,1310 1200,1380" fill="var(--brand-red)"/>
    <polygon points="448,1308 1205,1308 1205,1378" fill="var(--deep-red)"/>

    <text class="brand-name" x="395" y="1015" font-size="54" text-anchor="middle">Bright Oak Fitness</text>
    <text class="tagline" x="195" y="1094" font-size="42">"Stronger Every Day"</text>

    <g class="contact-icon icon-pin">
      <circle class="icon-ring" cx="756" cy="997" r="22"/>
      <path class="icon-line" d="M756,1008 C748,998 748,992 748,989 A8,8 0 0 1 764,989 C764,992 764,998 756,1008 Z"/>
      <path class="icon-line" d="M744,1006 Q756,1014 768,1006"/>
    </g>
    <text class="contact-text" x="792" y="993">2817 Mossgrove Bend Road</text>
    <text class="contact-text" x="795" y="1025">Lakemont, Oregon 97190</text>

    <g class="contact-icon icon-phone">
      <circle class="icon-ring" cx="700" cy="1087" r="22"/>
      <path class="icon-glyph" d="M689,1076 l6,-2 4,8 -4,3 q3,7 10,10 l3,-4 8,4 -2,6 q-18,2 -25,-25 z"/>
    </g>
    <text class="contact-text" x="735" y="1099">541-555-Jump (5867)</text>

    <g class="contact-icon icon-mail">
      <circle class="icon-ring" cx="646" cy="1164" r="22"/>
      <rect class="icon-glyph" x="633" y="1155" width="24" height="17" rx="2"/>
      <path d="M633,1156 L645,1165 L657,1156" stroke="var(--card-black)" stroke-width="2" fill="none"/>
    </g>
    <text class="contact-text" x="681" y="1176">info@brightoakfitness.example</text>

    <g class="contact-icon icon-globe">
      <circle class="icon-ring" cx="591" cy="1241" r="22"/>
      <circle class="icon-line" cx="591" cy="1241" r="15"/>
      <ellipse class="icon-line" cx="591" cy="1241" rx="6" ry="15"/>
      <path class="icon-line" d="M576,1241 H606 M579,1233 H603 M579,1249 H603"/>
    </g>
    <text class="contact-text" x="628" y="1253">www.brightoakfitness.example</text>
  </g>
</svg>
</body>
</html>
```